Glass window Vinyl

We are in need of window vinyls for the building shown in the photos. The current vinyls will come down, and we will install the new signage created by this process. We need to advertise:

"Harwell's Landing Pop Up Market"

Then, below that, it should say for rental inquiries call : 555.613.0872 with our logo which is attached along with our colors and brand guidelines. You may add more color to the Harwells landing pop up market signage if appropriate. It should be large enough to be easily read from the road by those passing by.

```html
<!DOCTYPE html>
<html lang="en">
<head>
<meta charset="utf-8">
<title>Harwell's Landing Pop Up Market – Window Sign</title>
<link rel="stylesheet" href="https://fonts.googleapis.com/css2?family=Oswald:wght@600&family=Montserrat:wght@500;600&family=Krona+One&display=swap">
<style>
  :root {
    --backdrop: #dddddd;
    --navy: #0d4050;
    --gold: #b89f6b;
    --white: #ffffff;
  }
  html, body {
    margin: 0;
    padding: 0;
    width: 1174px;
    height: 1200px;
    overflow: hidden;
    background: var(--backdrop);
  }
  .window-sign {
    position: absolute;
    left: 275px;
    top: 288px;
    width: 624px;
    height: 623px;
    display: block;
  }
  .sign-panel { fill: var(--white); }
  .header-band { fill: var(--navy); }
  .header-accent { fill: var(--gold); }
  .market-title {
    font-family: 'Oswald', 'Arial Narrow', sans-serif;
    font-weight: 600;
    font-size: 70px;
    fill: var(--white);
  }
  .inquiry-label {
    font-family: 'Montserrat', Arial, sans-serif;
    font-weight: 600;
    font-size: 29px;
    letter-spacing: -0.5px;
    fill: var(--navy);
  }
  .call-label { fill: var(--gold); }
  .phone-number {
    font-family: 'Krona One', 'Arial Black', sans-serif;
    font-size: 46px;
    fill: var(--navy);
  }
  .rule { fill: var(--gold); }
  .company-mark { fill: var(--gold); }
  .company-name {
    font-family: 'Montserrat', Arial, sans-serif;
    font-weight: 500;
    font-size: 19px;
    letter-spacing: 4px;
    fill: var(--navy);
  }
</style>
</head>
<body>
  <svg class="window-sign" viewBox="0 0 624 623" xmlns="http://www.w3.org/2000/svg" aria-label="Harwell's Landing Pop Up Market – for rental inquiries call 555.613.0872">
    <rect class="sign-panel" x="0" y="0" width="624" height="623"/>

    <!-- header chevron -->
    <polygon class="header-accent" points="0,245 624,245 313,317"/>
    <polygon class="header-band" points="0,0 624,0 624,245 313,303 0,245"/>

    <text class="market-title" x="312" y="124" text-anchor="middle">Harwell's</text>
    <text class="market-title" x="312" y="201" text-anchor="middle" textLength="549" lengthAdjust="spacingAndGlyphs">Landing Pop Up Market</text>

    <!-- rental contact -->
    <text class="inquiry-label" x="312" y="374" text-anchor="middle" textLength="341" lengthAdjust="spacingAndGlyphs">FOR RENTAL INQUIRIES</text>
    <text class="inquiry-label call-label" x="312" y="409" text-anchor="middle">CALL</text>
    <text class="phone-number" x="312" y="472" text-anchor="middle" textLength="552" lengthAdjust="spacingAndGlyphs">555.613.0872</text>

    <rect class="rule" x="38" y="486" width="556" height="4"/>
    <rect class="rule" x="38" y="494" width="556" height="2"/>

    <!-- company -->
    <rect class="company-mark" x="303" y="512" width="18" height="18"/>
    <text class="company-name" x="312" y="566" text-anchor="middle">BIRCHWOOD ROW PROPERTIES</text>
  </svg>
</body>
</html>
```